Hollowbrook Renderworks Wordpress Design

I would like a design for my friends company. He has just had his logo designed and really likes the following website.

www.tbr-skimcoat.co.uk

Something similar to this design would be ideal but open to additional ideas. The website shown has all the relevant content.

We have 20 years of experience and can provide a number of photos for work we have done.

More photos will be provided upon request.

Target Market(s)

Homeowners

Industry/Entity Type

Trade

Font styles to use
Sans Serif

Colors
3176b5
85cae6
85abd2
eaf1f7

Requirements
Must have
• look at www.tbr-skimcoat.co.uk
Nice to have
Should not have
• N/A

```html
<!DOCTYPE html>
<html lang="en">
<head>
<meta charset="utf-8">
<title>Hollowbrook Renderworks</title>
<link href="https://fonts.googleapis.com/css2?family=Cinzel:wght@600;700&family=Lato:ital,wght@0,400;0,700;1,400&display=swap" rel="stylesheet">
<style>
:root{
  --blue:#2f609b;
  --blue-dark:#254f84;
  --sky:#d3e4f2;
  --pale:#eaf1f7;
  --ink:#333;
  --muted:#666;
  --grey:#b9b9b9;
  --grey-dark:#a4a4a4;
  --footer:#2b2b2b;
  --footer-text:#bbb;
  --link:#5aa0d8;
}
*{box-sizing:border-box;margin:0;padding:0}
html,body{width:1200px;height:3636px;overflow:hidden}
body{font-family:"Lato",Arial,sans-serif;color:var(--ink);background:#fff;position:relative}
.wrap{width:940px;margin:0 auto;position:relative}
.section-title{font-family:"Cinzel",Georgia,serif;font-weight:700;font-size:24px;letter-spacing:2px;text-align:center;color:#222;text-transform:uppercase}
.section-title::after{content:"";display:block;width:360px;height:1px;background:#ccc;margin:14px auto 0}
.section-title span{display:block;width:48px;height:4px;background:var(--blue);margin:-2px auto 0;position:relative;top:16px}
.light .section-title{color:#fff}.light .section-title::after{background:rgba(255,255,255,.4)}
.btn{display:inline-block;background:var(--blue);color:#fff;font-size:17px;padding:13px 34px;white-space:nowrap}

/* header */
.site-header{height:109px;position:relative;border-bottom:1px solid #ddd}
.brand{position:absolute;left:131px;top:24px;font-weight:700;color:var(--blue);font-size:25px;line-height:28px;letter-spacing:1px}
.brand .sq{display:inline-block;width:14px;height:14px;background:var(--blue);margin-left:8px}
.top-contact{position:absolute;top:22px;font-size:14px;color:#444;display:flex;align-items:center;gap:10px;white-space:nowrap}
.top-contact svg{width:22px;height:22px}
.nav{position:absolute;top:74px;left:485px;display:flex;font-family:"Cinzel",serif;font-weight:600;font-size:14px;letter-spacing:1px}
.nav a{color:#333;text-decoration:none;padding:0 18px;border-right:1px solid #ddd;line-height:20px}
.nav a:last-child{border:none}
.nav a.active{color:var(--blue);border-bottom:2px solid var(--blue)}

/* hero */
.hero{height:468px;position:relative;overflow:hidden}
.hero-photo{position:absolute;inset:0;background:linear-gradient(90deg,#c9b8a8 0%,#e9ecef 30%,#f1f3f5 50%,#dde1e5 75%,#cfd5db 100%)}
.slide-arrow{position:absolute;top:195px;width:34px;height:34px;background:#222;display:flex;align-items:center;justify-content:center}
.callback{position:absolute;left:650px;top:66px;width:417px;height:269px;background:rgba(70,70,70,.85);border-radius:6px;padding:16px 20px;color:#fff}
.callback h2{font-weight:400;font-size:19px;margin-bottom:12px;white-space:nowrap}
.callback .field{height:32px;background:#fff;margin:0 0 10px 20px;font-size:12px;color:#888;padding:8px 10px}
.captcha-row{display:flex;gap:10px;margin-left:20px;margin-bottom:12px}
.captcha{width:86px;height:32px;background:linear-gradient(90deg,#bbb,#eee)}
.captcha-row .field{flex:1;margin:0}
.callback-actions{display:flex;align-items:center;gap:9px;margin-left:20px;font-size:15px;white-space:nowrap}
.callback-actions .btn{padding:7px 18px;font-weight:700;font-size:16px}
.callback-actions svg{width:24px;height:24px;flex:none}
.callback-actions .phone{font-size:16px}
.hero-caption{position:absolute;left:0;right:0;bottom:0;height:68px;background:rgba(30,30,30,.72);color:#fff;text-align:center;font-size:22px;line-height:27px;padding-top:7px}

/* services */
.services{height:730px;padding-top:50px}
.service-grid{display:grid;grid-template-columns:repeat(3,1fr);margin-top:62px;row-gap:48px}
.service{text-align:center}
.service .icon{width:130px;height:130px;border-radius:50%;background:var(--grey);margin:0 auto 20px;display:flex;align-items:center;justify-content:center}
.service .icon.active{background:var(--blue)}
.service .icon svg{width:64px;height:64px}
.service h3{color:var(--blue);font-size:19px;font-weight:700;line-height:24px}
.service p{font-size:13px;line-height:17px;color:#444;width:230px;margin:4px auto 0}

/* welcome */
.welcome{height:312px;background:var(--sky);padding-top:44px;text-align:center}
.welcome .section-title::after{display:none}
.welcome p{font-size:13.5px;line-height:19px;color:#444;margin:30px 0 30px}

/* video */
.video{height:444px;position:relative;color:#fff}
.video-bg{position:absolute;inset:0;background:linear-gradient(90deg,#3a3631,#25231f 50%,#1b1a18)}
.video .wrap{padding-top:42px}
.video-copy{position:absolute;left:0;top:155px;width:490px}
.video-copy h3{font-size:22px;font-weight:700;margin-bottom:14px}
.video-copy p{font-size:13.5px;line-height:19px;margin-bottom:40px}
.monitor{position:absolute;left:566px;top:131px;width:371px;height:267px}
.monitor .screen{position:absolute;left:0;top:0;width:371px;height:236px;background:#1a1a1a;border-radius:8px;padding:12px}
.monitor .picture{width:100%;height:100%;background:linear-gradient(135deg,#c8ccd0,#eef0f2 50%,#b4b8bd);display:flex;align-items:center;justify-content:center}
.monitor .stand{position:absolute;left:0;top:236px;width:371px;height:31px;background:linear-gradient(180deg,#d7d9dc,#a9acb0);border-radius:0 0 8px 8px}

/* recent work */
.recent{height:366px;padding-top:50px}
.gallery{display:flex;margin-top:56px;height:187px}
.gallery div{height:100%;position:relative}
.gallery .overlay{position:absolute;inset:0;display:flex;align-items:center;justify-content:center;text-align:center;color:#fff;font-size:14px;font-weight:700;padding:0 30px}

/* testimonials */
.testimonials{height:347px;background:var(--blue);padding-top:46px;text-align:center;color:#fff;position:relative}
.avatar{width:90px;height:90px;border-radius:50%;background:#dfe6ee;margin:42px auto 24px;border:3px solid #fff}
.testimonials blockquote{font-style:italic;font-size:19px}
.testimonials p{font-style:italic;font-size:12px;line-height:17px;margin-top:8px;color:#dbe6f2}
.t-arrow{position:absolute;top:175px;width:30px;height:30px}

/* clients */
.clients{height:215px;padding-top:36px}
.client-row{display:flex;justify-content:space-between;align-items:center;margin-top:60px}
.client{display:flex;align-items:center;gap:12px;font-size:36px;color:#555;white-space:nowrap}
.client i{display:inline-block;width:30px;height:30px;background:#555;border-radius:50%}

/* accreditation */
.accred{height:274px;background:var(--sky);padding-top:56px}
.badges{display:flex;justify-content:space-around;margin-top:62px;padding:0 60px}
.badge{width:165px;height:85px}

/* footer */
.site-footer{height:315px;background:var(--footer);color:var(--footer-text);position:relative}
.footer-col{position:absolute;top:38px;font-size:12px;line-height:16px}
.footer-col h4{font-family:"Cinzel",serif;color:#fff;font-size:15px;letter-spacing:1px;margin-bottom:26px;white-space:nowrap}
.footer-col ul{list-style:none}
.footer-col li{margin-bottom:13px;color:#ddd;font-size:13px}
.footer-col li::before{content:"› ";color:#888}
.feed{margin-bottom:14px}
.feed a,.news a{color:var(--link);text-decoration:none;font-weight:700}
.news{margin-bottom:12px}
.contact-line{display:flex;gap:10px;align-items:flex-start;margin-bottom:14px;color:#ddd;font-size:13px}
.contact-line svg{width:18px;height:18px;flex:none}
.copyright{position:absolute;left:0;right:0;bottom:0;height:56px;background:var(--blue-dark);color:#e5edf6;font-size:13px}
.copyright .wrap{display:flex;justify-content:space-between;align-items:center;height:56px}
.social{display:flex;gap:8px}
.social span{width:30px;height:30px;border-radius:50%;background:#fff;display:block}
</style>
</head>
<body>

<header class="site-header">
  <div class="brand">HOLLOWBROOK<span class="sq"></span><br>RENDERWORKS</div>
  <div class="top-contact" style="left:686px">
    <svg viewBox="0 0 24 24"><circle cx="12" cy="12" r="11" fill="#e3e3e3"/><rect x="6" y="8" width="12" height="8" fill="none" stroke="#555" stroke-width="1.5"/><path d="M6 8l6 5 6-5" fill="none" stroke="#555" stroke-width="1.5"/></svg>
    info@hollowbrookrender.co.uk
  </div>
  <div class="top-contact" style="left:945px">
    <svg viewBox="0 0 24 24"><circle cx="12" cy="12" r="11" fill="#e3e3e3"/><path d="M8 6c-1 1-1 3 1 6s4 5 6 5l2-2-2.5-2-1.5 1c-1-.5-3-2.5-3.5-3.5l1-1.5L8.5 6z" fill="#555"/></svg>
    (123) 456 7890
  </div>
  <nav class="nav">
    <a class="active">HOME</a><a>ABOUT US</a><a>SERVICES</a><a>TESTIMONIALS</a><a>CONTACT US</a>
  </nav>
</header>

<section class="hero">
  <div class="hero-photo" role="img" aria-label="Plasterer in a white cap smoothing a wall with a trowel"></div>
  <div class="slide-arrow" style="left:8px"><svg width="14" height="14" viewBox="0 0 14 14"><path d="M9 2L4 7l5 5" stroke="#fff" stroke-width="2.5" fill="none"/></svg></div>
  <div class="slide-arrow" style="right:8px"><svg width="14" height="14" viewBox="0 0 14 14"><path d="M5 2l5 5-5 5" stroke="#fff" stroke-width="2.5" fill="none"/></svg></div>
  <form class="callback">
    <h2>Let us call you, just fill in the boxes below!</h2>
    <div class="field">Your Name</div>
    <div class="field">Your Phone Number</div>
    <div class="captcha-row"><div class="captcha" role="img" aria-label="Security code"></div><div class="field"></div></div>
    <div class="callback-actions">
      <span class="btn">Submit</span><span>Or Call Today</span>
      <svg viewBox="0 0 24 24"><circle cx="12" cy="12" r="11" fill="none" stroke="#fff" stroke-width="1.5"/><path d="M8 6c-1 1-1 3 1 6s4 5 6 5l2-2-2.5-2-1.5 1c-1-.5-3-2.5-3.5-3.5l1-1.5L8.5 6z" fill="#fff"/></svg>
      <span class="phone">(123) 456 7890</span>
    </div>
  </form>
  <div class="hero-caption">We Specialise In Internal Plastering, Rendering &amp; Thin Coat Insulated Render Systems, Serving<br>Both The Domestic And Commercial Markets</div>
</section>

<section class="services">
  <div class="wrap">
    <h2 class="section-title">Our Services<span></span></h2>
    <div class="service-grid">
      <div class="service">
        <div class="icon active" role="img" aria-label="Tools icon"><svg viewBox="0 0 64 64"><path d="M14 50L36 28" stroke="#fff" stroke-width="7" stroke-linecap="round"/><circle cx="42" cy="22" r="10" fill="none" stroke="#fff" stroke-width="6"/><path d="M50 50L30 30" stroke="#fff" stroke-width="5" stroke-linecap="round"/></svg></div>
        <h3>Rendering</h3><p>Lorem ipsum dolor sit amet, consectetuer adipiscing elit, sed diam nonummy nibh euismod tincidunt ut</p></div>
      <div class="service">
        <div class="icon" role="img" aria-label="Building icon"><svg viewBox="0 0 64 64"><rect x="16" y="12" width="24" height="42" fill="#fff"/><rect x="40" y="24" width="10" height="30" fill="#eee"/><g stroke="#b9b9b9" stroke-width="2"><path d="M20 20h16M20 28h16M20 36h16M20 44h16"/></g></svg></div>
        <h3>Skimming</h3><p>Lorem ipsum dolor sit amet, consectetuer adipiscing elit, sed diam nonummy nibh euismod tincidunt ut</p></div>
      <div class="service">
        <div class="icon" role="img" aria-label="Pointing trowel icon"><svg viewBox="0 0 64 64"><path d="M12 44L40 16l8 8-28 28z" fill="#fff"/><path d="M44 20l10-10" stroke="#fff" stroke-width="5" stroke-linecap="round"/></svg></div>
        <h3>Repointing</h3><p>Lorem ipsum dolor sit amet, consectetuer adipiscing elit, sed diam nonummy nibh euismod tincidunt ut</p></div>
      <div class="service">
        <div class="icon" role="img" aria-label="Chimney icon"><svg viewBox="0 0 64 64"><path d="M8 36L32 16l24 20" fill="none" stroke="#fff" stroke-width="5"/><rect x="40" y="12" width="9" height="16" fill="#fff"/><rect x="16" y="36" width="32" height="18" fill="#fff"/></svg></div>
        <h3>Chimney<br>Repairs</h3><p>Lorem ipsum dolor sit amet, consectetuer adipiscing elit, sed diam nonummy nibh euismod tincidunt ut</p></div>
      <div class="service">
        <div class="icon" role="img" aria-label="Plasterboard icon"><svg viewBox="0 0 64 64"><rect x="12" y="10" width="18" height="44" fill="#fff"/><rect x="34" y="10" width="18" height="44" fill="#fff"/></svg></div>
        <h3>Plasterboard /<br>Dry Lining</h3><p>Lorem ipsum dolor sit amet, consectetuer adipiscing elit, sed diam nonummy nibh euismod tincidunt ut</p></div>
      <div class="service">
        <div class="icon" role="img" aria-label="Brick wall icon"><svg viewBox="0 0 64 64"><rect x="14" y="10" width="36" height="44" fill="#fff"/><g stroke="#b9b9b9" stroke-width="2"><path d="M14 21h36M14 32h36M14 43h36M32 10v11M23 21v11M41 21v11M32 32v11M23 43v11M41 43v11"/></g></svg></div>
        <h3>External Wall<br>Insulation</h3><p>Lorem ipsum dolor sit amet, consectetuer adipiscing elit, sed diam nonummy nibh euismod tincidunt ut</p></div>
    </div>
  </div>
</section>

<section class="welcome">
  <div class="wrap">
    <h2 class="section-title">Welcome to Hollowbrook Renderworks</h2>
    <p>Lorem ipsum dolor sit amet, consectetuer adipiscing elit, sed diam nonummy nibh euismod tincidunt ut laoreet dolore magna aliquam erat volutpat. Ut wisi enim ad minim veniam, quis nostrud exerci tation ullamcorper suscipit lobortis nisl ut aliquip ex ea commodo consequat. Duis autem vel eum iriure dolor in hendrerit in vulputate velit esse molestie consequat, vel illum dolore eu feugiat nulla facilisis at vero eros et accumsan et iusto odio dignissim qui blandit praesent luptatum zzril delenit augue duis dolore te feugait nulla facilisi.</p>
    <span class="btn">Read More</span>
  </div>
</section>

<section class="video light">
  <div class="video-bg" role="img" aria-label="Dim interior of a room being plastered"></div>
  <div class="wrap">
    <h2 class="section-title">Hollowbrook Renderworks Monthly Video Tips<span></span></h2>
    <div class="video-copy">
      <h3>Introduction into Re-pointing</h3>
      <p>Lorem ipsum dolor sit amet, consectetuer adipiscing elit, sed diam nonummy nibh euismod tincidunt ut laoreet dolore magna aliquam erat volutpat. Ut wisi enim ad minim veniam, quis nostrud exerci tation ullamcorper suscipit lobortis nisl ut aliquip ex ea commodo consequat.</p>
      <span class="btn">Contact Us Today Free Quote</span>
    </div>
    <div class="monitor">
      <div class="screen"><div class="picture" role="img" aria-label="Video of a plasterer trowelling a wall"><svg width="48" height="48" viewBox="0 0 48 48"><circle cx="24" cy="24" r="23" fill="rgba(40,40,40,.75)"/><path d="M19 14l14 10-14 10z" fill="#fff"/></svg></div></div>
      <div class="stand"></div>
    </div>
  </div>
</section>

<section class="recent">
  <div class="wrap">
    <h2 class="section-title">Hollowbrook Renderworks Recent Work?<span></span></h2>
    <div class="gallery">
      <div style="width:272px;background:linear-gradient(160deg,#9fb6cc,#8a6a4e 55%,#5e4633)" role="img" aria-label="Stone house with rendered gable"></div>
      <div style="width:194px;background:linear-gradient(180deg,#6d665a,#3f3a32)" role="img" aria-label="Rendered house front"><span class="overlay">Lorem ipsum dolor sit amet, consectetuer</span></div>
      <div style="width:240px;background:linear-gradient(180deg,#d8d4cc,#3b2c22 60%,#6a5847)" role="img" aria-label="Mock Tudor house exterior"></div>
      <div style="width:234px;background:linear-gradient(180deg,#e8c4ad,#d49f82)" role="img" aria-label="Plasterer skimming an interior wall"></div>
    </div>
  </div>
</section>

<section class="testimonials light">
  <div class="wrap">
    <h2 class="section-title">Client Testimonials<span></span></h2>
    <div class="avatar" role="img" aria-label="Client portrait"></div>
    <blockquote>Vestibulum porta, diam quis auctor ultricies, dui quam dapibus ligula, consectetur</blockquote>
    <p>Lorem ipsum dolor sit amet, consectetuer adipiscing elit. Integer venenatis tincidunt elit, aliquam semper quam pulvinar id. Aliquam erat volutpat. Integer<br>nulla urna, sagittis sed viverra quis, tincidunt vel felis. Pellentesque eleifend sem ut diam bibendum, non sagittis sapien pellentesque. Etiam semper</p>
  </div>
  <svg class="t-arrow" style="left:126px" viewBox="0 0 30 30"><path d="M19 5L9 15l10 10" stroke="#fff" stroke-width="4" fill="none"/></svg>
  <svg class="t-arrow" style="right:126px" viewBox="0 0 30 30"><path d="M11 5l10 10-10 10" stroke="#fff" stroke-width="4" fill="none"/></svg>
</section>

<section class="clients">
  <div class="wrap">
    <h2 class="section-title">Our Clients<span></span></h2>
    <div class="client-row">
      <div class="client">Arklane</div>
      <div class="client"><i></i>Stonefield</div>
      <div class="client"><i></i>Meridale</div>
      <div class="client"><i></i>Stonefield</div>
    </div>
  </div>
</section>

<section class="accred">
  <div class="wrap">
    <h2 class="section-title">Accreditation and Memberships<span></span></h2>
    <div class="badges">
      <svg class="badge" viewBox="0 0 165 85" role="img" aria-label="Business network membership badge"><rect x="10" y="5" width="145" height="75" fill="#b01f2e"/></svg>
      <svg class="badge" viewBox="0 0 165 85" role="img" aria-label="Construction training board badge"><rect x="5" y="8" width="155" height="70" rx="35" fill="#5a3f8e"/></svg>
      <svg class="badge" viewBox="0 0 165 85" role="img" aria-label="Health and safety scheme badge"><ellipse cx="82" cy="43" rx="75" ry="38" fill="#5b2d86"/></svg>
    </div>
  </div>
</section>

<footer class="site-footer">
  <div class="footer-col" style="left:131px">
    <h4>QUICK LINKS</h4>
    <ul><li>Home</li><li>About Us</li><li>Services</li><li>Testimonials</li><li>Contact Us</li></ul>
  </div>
  <div class="footer-col" style="left:291px;width:260px">
    <h4>TWITTER FEEDS</h4>
    <div class="feed"><a>Lorem Ipsum</a> is simply dummy text. Tempor - Tweet tweet -<br><a>http://hbrender.co/tips56</a><br>12 minutes ago</div>
    <div class="feed"><a>Lorem Ipsum</a> is simply dummy text. Tempor - Tweet tweet -<br><a>http://hbrender.co/tips56</a><br>12 minutes ago</div>
  </div>
  <div class="footer-col" style="left:589px;width:230px">
    <h4>NEWS &amp; UPDATES</h4>
    <div class="news"><a>Lorem Ipsum Dolor Consecte</a><br>Sed ut perspiciatis unde omnis iste natus error sit voluptatem ...<br><br>21 Mar 2016</div>
    <div class="news"><a>Lorem Ipsum Dolor Consecte</a><br>Sed ut perspiciatis unde omnis iste natus error sit voluptatem ...<br><br>21 Mar 2016</div>
  </div>
  <div class="footer-col" style="left:853px;width:230px">
    <h4>CONTACT DETAILS</h4>
    <div class="contact-line"><svg viewBox="0 0 18 18"><path d="M9 1a6 6 0 0 0-6 6c0 4 6 10 6 10s6-6 6-10a6 6 0 0 0-6-6z" fill="var(--link)"/><circle cx="9" cy="7" r="2" fill="#2b2b2b"/></svg><span><b style="color:#fff">Hollowbrook Renderworks</b><br>123 PG Duis aute irur dolore<br>srephenderit amit in voluptate</span></div>
    <div class="contact-line"><svg viewBox="0 0 18 18"><path d="M5 2c-1 1-2 3 1 7s6 6 7 6l2-2-3-2-1.5 1c-1-.5-3-2.5-3.5-3.5L8 7 5.5 2z" fill="var(--link)"/></svg>(123) 456 7890</div>
    <div class="contact-line"><svg viewBox="0 0 18 18"><rect x="3" y="6" width="12" height="7" fill="var(--link)"/><rect x="5" y="2" width="8" height="4" fill="var(--link)"/></svg>(123) 456 7890</div>
    <div class="contact-line"><svg viewBox="0 0 18 18"><circle cx="9" cy="9" r="8" fill="var(--link)"/><rect x="5" y="6" width="8" height="6" fill="#2b2b2b"/></svg>info@hollowbrookrender.co.uk</div>
  </div>
  <div class="copyright">
    <div class="wrap">
      <span>Copyright © 2016 Hollowbrook Renderworks. All Rights Reserved.</span>
      <div class="social"><span></span><span></span><span></span></div>
    </div>
  </div>
</footer>

</body>
</html>
```